stationary deign for trucking company

im a trucking company looking for a professional set of stationary designs i deliver goods from point a to b
Updates

When submitting stationary designs I need envelope design, letterhead, cards, I’d badge etc

Industry/Entity Type

Trucking Company

Requirements
Must have
• must have letter head, business card, envelope, fax sheet, id badge, folder, thank you card, notebook, invoice sheet.
Nice to have
• nice to have them all custom made (letterhead,envelope, business card, I’d badge etc
Should not have
• must not have prepaid sign want i unique design for items

```html
<!DOCTYPE html>
<html lang="en">
<head>
<meta charset="utf-8">
<title>Halvorsen Freight – Business Card</title>
<link rel="stylesheet" href="https://fonts.googleapis.com/css2?family=Arimo:wght@400;700&family=Roboto:wght@400&display=swap">
<style>
  :root {
    --page-bg: #d9d9d9;
    --ink: #000000;
    --paper: #ffffff;
    --brand-blue: #0756a5;
    --name-blue: #0d57a8;
  }
  * { margin: 0; padding: 0; box-sizing: border-box; }
  html, body {
    width: 1125px;
    height: 1200px;
    overflow: hidden;
    background: var(--page-bg);
    font-family: "Arimo", Arial, sans-serif;
  }
  .card {
    position: absolute;
    left: 156px;
    width: 825px;
    height: 471px;
    overflow: hidden;
  }
  .card-front { top: 106px; background: var(--paper); }
  .card-back  { top: 639px; background: var(--brand-blue); }

  .front-panel {
    position: absolute;
    inset: 0;
    width: 825px;
    height: 471px;
  }

  .holder-name {
    position: absolute;
    left: 43px;
    top: 72px;
    font-size: 31px;
    font-weight: 700;
    color: var(--name-blue);
    letter-spacing: 0.2px;
  }
  .holder-title {
    position: absolute;
    left: 44px;
    top: 107px;
    font-size: 21px;
    color: var(--paper);
  }
  .address {
    position: absolute;
    left: 44px;
    top: 172px;
    font-size: 19.5px;
    line-height: 25px;
    color: var(--paper);
  }
  .contact-list {
    position: absolute;
    left: 44px;
    top: 230px;
    list-style: none;
  }
  .contact-list li {
    display: flex;
    align-items: center;
    height: 26.3px;
    font-size: 19.5px;
    color: var(--paper);
  }
  .contact-list svg {
    width: 20px;
    height: 20px;
    margin-right: 12px;
    fill: var(--name-blue);
    flex: none;
  }

  .front-brand {
    position: absolute;
    left: 404px;
    top: 206px;
    display: flex;
    align-items: center;
    gap: 16px;
  }
  .brand-square {
    width: 34px;
    height: 34px;
    background: var(--brand-blue);
  }
  .brand-name {
    font-size: 36px;
    font-weight: 700;
    color: var(--ink);
    letter-spacing: 3px;
  }

  .back-brand {
    position: absolute;
    left: 0;
    right: 0;
    top: 196px;
    text-align: center;
    font-size: 66px;
    font-weight: 700;
    color: var(--paper);
    letter-spacing: 4px;
  }
  .back-url {
    position: absolute;
    left: 0;
    right: 0;
    top: 405px;
    text-align: center;
    font-family: "Roboto", Arial, sans-serif;
    font-size: 18px;
    color: var(--paper);
    letter-spacing: 8px;
  }
</style>
</head>
<body>

<section class="card card-front">
  <svg class="front-panel" viewBox="0 0 825 471" aria-hidden="true">
    <polygon points="0,0 505,0 329,227 509,471 0,471" fill="var(--ink)"/>
    <polyline points="497,-4 320,227 500,475" fill="none" stroke="var(--paper)" stroke-width="2"/>
    <polyline points="517,-4 339,227 521,475" fill="none" stroke="var(--ink)" stroke-width="5"/>
  </svg>

  <h1 class="holder-name">DANIEL REYES</h1>
  <p class="holder-title">OWNER/OPERATOR</p>
  <p class="address">2140 Birchwood Road<br>Fairview, Oregon 97024</p>

  <ul class="contact-list">
    <li>
      <svg viewBox="0 0 24 24"><path d="M6.6 10.8a15.1 15.1 0 0 0 6.6 6.6l2.2-2.2a1 1 0 0 1 1-.25 11.4 11.4 0 0 0 3.6.57 1 1 0 0 1 1 1V20a1 1 0 0 1-1 1A17 17 0 0 1 3 4a1 1 0 0 1 1-1h3.5a1 1 0 0 1 1 1c0 1.25.2 2.45.57 3.6a1 1 0 0 1-.25 1z"/></svg>
      503 214 7781
    </li>
    <li>
      <svg viewBox="0 0 24 24"><path d="M7 1h10a2 2 0 0 1 2 2v18a2 2 0 0 1-2 2H7a2 2 0 0 1-2-2V3a2 2 0 0 1 2-2zm0 3v14h10V4zm5 16.2a1 1 0 1 0 0 .01z"/></svg>
      503 877 2190
    </li>
    <li>
      <svg viewBox="0 0 24 24"><path d="M6 2h9l3 3v4H6zM4 10h16a2 2 0 0 1 2 2v6h-4v4H6v-4H2v-6a2 2 0 0 1 2-2zm4 6v4h8v-4z"/></svg>
      503 655 4032
    </li>
    <li>
      <svg viewBox="0 0 24 24"><path d="M2 6h20v12H2zm2 1.5v.4l8 5 8-5v-.4z"/></svg>
      daniel@halvorsenfreight.com
    </li>
    <li>
      <svg viewBox="0 0 24 24"><path d="M12 2a10 10 0 1 0 0 20 10 10 0 0 0 0-20zm-1 17.9A8 8 0 0 1 4.2 10L9 15v1a2 2 0 0 0 2 2zm6.9-2.5A2 2 0 0 0 16 16h-1v-3a1 1 0 0 0-1-1H8v-2h2a1 1 0 0 0 1-1V7h2a2 2 0 0 0 2-2v-.4a8 8 0 0 1 2.9 12.8z"/></svg>
      www.halvorsenfreight.com
    </li>
  </ul>

  <div class="front-brand">
    <span class="brand-square" aria-hidden="true"></span>
    <span class="brand-name">HALVORSEN FREIGHT</span>
  </div>
</section>

<section class="card card-back">
  <p class="back-brand">HALVORSEN</p>
  <p class="back-url">www.halvorsenfreight.com</p>
</section>

</body>
</html>
```